KPV Construction we build lodges in Botswana

We need a Design Layout only with Categories where we can update each projects photos.... We have a web address and a host - kpv.construction

```html
<!DOCTYPE html>
<html lang="en">
<head>
<meta charset="utf-8">
<title>KPV Construction – We build lodges in Botswana</title>
<link href="https://fonts.googleapis.com/css2?family=Poppins:wght@500;600;700&family=Roboto:wght@400;500&display=swap" rel="stylesheet">
<style>
:root{
  --blue:#0b6dbf;
  --ink:#111418;
  --body:#3a3d42;
  --white:#ffffff;
  --accent:#f3b720;
  --icon-bg:#eef1f4;
  --footer-deep:#111315;
  --muted:#c9ccd0;
}
*{box-sizing:border-box;margin:0;padding:0}
html,body{width:1200px;height:2630px;overflow:hidden}
body{position:relative;background:var(--white);font-family:'Roboto',sans-serif;color:var(--body)}
.abs{position:absolute}

/* hero */
.hero{left:0;top:0;width:1200px;height:540px;
  background:linear-gradient(180deg,#5a5f6b 0%,#9a7a66 22%,#8b5a3a 48%,#6b4a2e 72%,#4b3a26 100%)}
.hero-shade{left:0;top:0;width:1200px;height:540px;background:linear-gradient(90deg,rgba(0,0,0,.35),rgba(0,0,0,.05) 60%)}
.topbar{left:0;top:0;width:1200px;height:34px;background:rgba(0,0,0,.55);color:var(--white);font-size:12px}
.topbar .item{position:absolute;top:0;height:34px;display:flex;align-items:center;gap:6px}
.topbar .dot{width:9px;height:9px;border-radius:50%;background:var(--white);display:inline-block;margin-left:6px}
.brand{left:180px;top:100px;font-family:'Poppins',sans-serif;font-weight:600;font-size:15px;letter-spacing:1px;color:var(--white);display:flex;align-items:center;gap:8px}
.brand .mark{width:22px;height:22px;background:var(--blue)}
.nav{top:46px;left:626px;font-size:13.5px;color:var(--white)}
.nav a{color:var(--white);text-decoration:none;position:absolute;white-space:nowrap}
.nav .active::after{content:"";position:absolute;left:0;right:0;bottom:-11px;height:2px;background:var(--blue)}
.hero-title{left:180px;top:180px;font-family:'Poppins',sans-serif;font-weight:700;font-size:55px;line-height:62px;color:var(--white)}
.hero-text{left:180px;top:314px;width:495px;font-size:13.5px;line-height:22px;color:var(--white)}
.btn-primary{left:180px;top:377px;width:146px;height:39px;border-radius:20px;background:var(--blue);color:var(--white);font-size:15px;font-weight:500;display:flex;align-items:center;justify-content:center}
.slider-dots{left:576px;top:512px;display:flex;gap:5px}
.slider-dots span{width:11px;height:11px;border-radius:50%;background:rgba(255,255,255,.6)}
.slider-dots .on{background:transparent;border:2px solid var(--white)}

/* intro */
.intro-title{left:150px;top:598px;width:355px;text-align:right;font-family:'Poppins',sans-serif;font-weight:600;font-size:26px;line-height:32px;color:var(--ink)}
.intro-rule{left:524px;top:596px;width:4px;height:72px;background:var(--blue)}
.intro-text{left:554px;top:590px;width:475px;font-size:13.5px;line-height:26px;color:var(--body)}

/* services */
.service{width:210px;text-align:center}
.service-icon{width:54px;height:54px;margin:0 auto;border-radius:50%;background:var(--icon-bg);border:2px solid var(--accent)}
.service h3{font-family:'Poppins',sans-serif;font-weight:600;font-size:14.5px;color:var(--ink);margin-top:24px}
.service p{font-size:12.5px;line-height:22px;margin-top:12px;padding:0 20px}

/* section headings */
.section-title{left:0;width:1200px;text-align:center;font-family:'Poppins',sans-serif;font-weight:600;font-size:28px;color:var(--ink)}
.section-rule{left:565px;width:70px;height:4px;background:var(--blue)}

/* projects */
.projects{left:0;top:1130px;width:1200px;height:475px;display:grid;grid-template-columns:repeat(4,300px);grid-template-rows:repeat(2,237.5px)}
.project-photo{width:100%;height:100%}
.projects-band{left:0;top:1605px;width:1200px;height:114px;background:var(--blue)}
.btn-outline{left:512px;top:1643px;width:176px;height:39px;border:2px solid var(--white);border-radius:20px;color:var(--white);font-size:15px;display:flex;align-items:center;justify-content:center}

/* blog */
.post{width:268px;top:1872px}
.post .photo{width:268px;height:163px}
.post .rule{width:36px;height:4px;background:var(--blue);margin-top:17px}
.post h3{font-family:'Poppins',sans-serif;font-weight:600;font-size:14px;line-height:21px;color:var(--ink);margin-top:14px;width:262px}
.post time{display:block;font-size:12.5px;color:var(--body);margin-top:8px}

/* footer */
.footer{left:0;top:2221px;width:1200px;height:357px;background:linear-gradient(180deg,#23272b,#1a1d1f 60%,#202419)}
.footer-brand{left:170px;top:150px;width:216px;text-align:center;font-family:'Poppins',sans-serif;font-weight:600;font-size:17px;letter-spacing:1px;white-space:nowrap;color:var(--blue)}
.footer-brand .mark{width:40px;height:40px;background:var(--blue);margin:0 auto 18px}
.footer h4{position:absolute;font-family:'Poppins',sans-serif;font-weight:500;font-size:17px;color:var(--white)}
.footer-rule{width:36px;height:4px;background:var(--blue)}
.footer-link{font-size:13.5px;color:var(--white)}
.contact{display:flex;align-items:center;gap:14px;font-size:14px;color:var(--white)}
.contact.strong{font-size:17px;font-weight:500}
.social{left:790px;top:2480px;display:flex;gap:24px}
.social span{width:12px;height:12px;border-radius:50%;background:var(--white)}
.social span.accent{background:var(--blue)}
.bottom-bar{left:0;top:2578px;width:1200px;height:52px;background:var(--footer-deep);border-top:1px solid #3a3e42;color:var(--muted);font-size:12.5px}
</style>
</head>
<body>

<div class="abs hero" role="img" aria-label="Photo of a wooden safari lodge deck with loungers under a large tree, overlooking a river at sunset"></div>
<div class="abs hero-shade"></div>

<div class="abs topbar">
  <div class="item" style="left:175px">
    <svg width="12" height="9" viewBox="0 0 12 9"><rect width="12" height="9" rx="1" fill="var(--blue)"/><path d="M0 0l6 5 6-5" stroke="#fff" fill="none"/></svg>
    Email Us info@kpvconstruction.com
  </div>
  <div class="item" style="left:398px">
    <svg width="10" height="10" viewBox="0 0 10 10"><path d="M2 0l2 3-1 1c1 1 2 2 3 3l1-1 3 2-1 2C4 10 0 6 0 1z" fill="var(--blue)"/></svg>
    Call Us: 555-214-7730
  </div>
  <div class="item" style="left:877px">Stay Connected: <span class="dot"></span><span class="dot"></span><span class="dot"></span></div>
</div>

<div class="abs brand"><span class="mark"></span>KPV CONSTRUCTION</div>

<nav class="abs nav">
  <a class="active" style="left:0">Home</a>
  <a style="left:63px">About Us</a>
  <a style="left:142px">Services</a>
  <a style="left:216px">Projects</a>
  <a style="left:290px">Blog</a>
  <a style="left:340px">Contact Us</a>
</nav>

<h1 class="abs hero-title">We build lodges<br>in Botswana</h1>
<p class="abs hero-text">Lorem ipsum dolor sit amet, consectetur adipiscing elit. Nunc ac eleifend ligula. Fusce semper, quam ac suscipit varius, mauris libero tincidunt est.</p>
<div class="abs btn-primary">Read More</div>
<div class="abs slider-dots"><span class="on"></span><span></span><span></span></div>

<h2 class="abs intro-title">Let’s Build<br>Your Lodge Together</h2>
<div class="abs intro-rule"></div>
<p class="abs intro-text">Aliquam tincidunt risus at est tincidunt, sed dapibus ligula pharetra. Cras condimentum dignissim turpis, vitae porta magna suscipit ultrices. Mauris egestas lectus ut felis faucibus luctus.</p>

<div class="abs service" style="left:158px;top:745px">
  <div class="service-icon" role="img" aria-label="Service icon for lodge renovation"></div>
  <h3>Lodge Renovation</h3>
  <p>Consectetur adipisicing elit, sed do eiusmod tempor incididunt ut labore et dolore magna aliqua. Ut enim ad minim veniam.</p>
</div>

<div class="abs service" style="left:381px;top:745px">
  <div class="service-icon" role="img" aria-label="Service icon for lodge construction"></div>
  <h3>Lodge Construction</h3>
  <p>Lorem ipsum dolor sit amet, consectetur adipisicing elit, sed do eiusmod tempor incid idunt ut labore et dolore magna aliqua.</p>
</div>

<div class="abs service" style="left:605px;top:745px">
  <div class="service-icon" role="img" aria-label="Service icon for lodge design"></div>
  <h3>Lodge Design</h3>
  <p>Consectetur adipisicing elit, sed do eiusmod tempor incididunt ut labore et dolore magna aliqua. Ut enim ad minim veniam.</p>
</div>

<div class="abs service" style="left:835px;top:745px">
  <div class="service-icon" role="img" aria-label="Service icon for lodge maintenance"></div>
  <h3>Lodge Maintenance</h3>
  <p>Lorem ipsum dolor sit amet, consectetur adipisicing elit, sed do eiusmod tempor incid idunt ut labore et dolore magna aliqua.</p>
</div>

<h2 class="abs section-title" style="top:1052px">Featured Projects</h2>
<div class="abs section-rule" style="top:1093px"></div>

<section class="abs projects">
  <div class="project-photo" role="img" aria-label="Project photo: curved timber lodge walkway among trees with an elephant nearby" style="background:linear-gradient(160deg,#8a6a45,#b4884f 50%,#6d5a3a)"></div>
  <div class="project-photo" role="img" aria-label="Project photo: thatched lodge deck with hammock overlooking green grassland" style="background:linear-gradient(180deg,#6f8aa0,#9a7048 45%,#5e4630)"></div>
  <div class="project-photo" role="img" aria-label="Project photo: lodge deck lit at dusk with lanterns and rocky garden" style="background:linear-gradient(170deg,#445066,#a0562c 55%,#6a3a1e)"></div>
  <div class="project-photo" role="img" aria-label="Project photo: thatched-roof chalets on a green lawn with a warthog" style="background:linear-gradient(180deg,#7f9dbb,#4f5b3b 45%,#6e8e3f)"></div>
  <div class="project-photo" role="img" aria-label="Project photo: riverside lodge in lush forest with an elephant in the water" style="background:linear-gradient(180deg,#5f8547,#3e6b32 55%,#556d58)"></div>
  <div class="project-photo" role="img" aria-label="Project photo: open-air lodge dining area glowing at night under trees" style="background:linear-gradient(180deg,#445a78,#5a4a34 55%,#8a6a3a)"></div>
  <div class="project-photo" role="img" aria-label="Project photo: woven dome-shaped lodge on stilts with wooden stairs" style="background:linear-gradient(180deg,#6f8fb0,#8a6844 50%,#5e4c3a)"></div>
  <div class="project-photo" role="img" aria-label="Project photo: large woven timber dome lodge with wide entrance steps" style="background:linear-gradient(180deg,#7a9ac0,#b08050 50%,#7a6a58)"></div>
</section>
<div class="abs projects-band"></div>
<div class="abs btn-outline">See All Projects</div>

<h2 class="abs section-title" style="top:1794px">KPV News Blog</h2>
<div class="abs section-rule" style="top:1834px"></div>

<article class="abs post" style="left:179px">
  <div class="photo" role="img" aria-label="Blog photo: safari tent bedroom with draped canopy bed" style="background:linear-gradient(180deg,#8a5a3a,#d9c4a6 60%,#6e4a30)"></div>
  <div class="rule"></div>
  <h3>Sed ultrices augue eget posuere venenatis finibus luctus leo, in</h3>
  <time>January 21, 2019</time>
</article>
<article class="abs post" style="left:468px">
  <div class="photo" role="img" aria-label="Blog photo: lodge lounge with woven chairs facing a sunset view" style="background:linear-gradient(180deg,#e0b27a,#a06a40 55%,#c9a27a)"></div>
  <div class="rule"></div>
  <h3>Nam risus risus, pretium vel sem<br>at, rhoncus mollis nunc</h3>
  <time>December 11, 2018</time>
</article>
<article class="abs post" style="left:758px">
  <div class="photo" role="img" aria-label="Blog photo: interior of curved timber lodge suite with sofa" style="background:linear-gradient(180deg,#c79a60,#8a6a48 55%,#5e4a36)"></div>
  <div class="rule"></div>
  <h3>Quisque pellentesque pretium<br>tortor, malesuada accumsan lore</h3>
  <time>November 22, 2018</time>
</article>

<footer class="abs footer" role="img" aria-label="Dark photo of a thatched lodge at night behind the footer">
  <div class="abs footer-brand"><div class="mark"></div>KPV CONSTRUCTION</div>

  <h4 style="left:454px;top:92px">Quick Links</h4>
  <div class="abs footer-rule" style="left:454px;top:122px"></div>
  <span class="abs footer-link" style="left:454px;top:150px">Home</span>
  <span class="abs footer-link" style="left:454px;top:184px">About Us</span>
  <span class="abs footer-link" style="left:454px;top:218px">Services</span>
  <span class="abs footer-link" style="left:581px;top:149px">Projects</span>
  <span class="abs footer-link" style="left:581px;top:183px">Blog</span>
  <span class="abs footer-link" style="left:581px;top:218px">Contact Us</span>

  <h4 style="left:758px;top:92px">Contact Info:</h4>
  <div class="abs footer-rule" style="left:758px;top:122px"></div>
  <div class="abs contact" style="left:758px;top:148px">
    <svg width="14" height="16" viewBox="0 0 14 16" fill="none" stroke="#fff" stroke-width="1.4"><path d="M7 15s5-5 5-9A5 5 0 002 6c0 4 5 9 5 9z"/><circle cx="7" cy="6" r="2"/></svg>
    48 Acacia Rd. Maun, Botswana
  </div>
  <div class="abs contact strong" style="left:758px;top:181px">
    <svg width="14" height="14" viewBox="0 0 14 14" fill="none" stroke="#fff" stroke-width="1.4"><path d="M3 1l2 3-1 2c1 2 2 3 4 4l2-1 3 2-1 2C6 13 1 8 1 2z"/></svg>
    Phone: (555) 318-2096
  </div>
  <div class="abs contact" style="left:758px;top:216px">
    <svg width="16" height="11" viewBox="0 0 16 11" fill="none" stroke="#fff" stroke-width="1.4"><rect x="1" y="1" width="14" height="9"/><path d="M1 1l7 5 7-5"/></svg>
    info@KPVconstruction.com
  </div>
</footer>
<div class="abs social"><span></span><span class="accent"></span><span></span></div>

<div class="abs bottom-bar">
  <span class="abs" style="left:170px;top:17px">© 2019. KPV Construction</span>
  <span class="abs" style="left:928px;top:17px">Privacy &nbsp;|&nbsp; Terms</span>
</div>

</body>
</html>
```